revised: 'eastgate joinwerks' logo -or- business card

we require a business card or a logo that can be used on a business card & other stationery

(i've just recently decided to open this contest up to logo designs as well - but if you have already been working on a card concept, please feel free to continue with it & submit!)

-

We design and build custom brackets and fixings for our customers and their castles, i.e. homes, offices, workshops, farms etc. Our products might be used to:
- brace or support structures, such as houses, decks, small bridges, etc.
- connect any building material to another
- or could simply be a unique piece that exists as a talking point

As part of our design process we would produce drawings/plans/blue prints/prototypes of the product. Our designs factor in multiple elements, from the materials being joined, the client's taste, and the overall durability demanded by the application - if necessary, the bracket may also be endorsed by a third party, such as a stuctural or mechanical engineer.

The build process takes part in our workshop and on the client's site - some elements may be manufactured off-site, depending on the design chosen and the materials used.

Our brackets are designed to our customers' tastes and could be made to be hidden within the structure or exposed to create interest. Our brackets can be large or small, or be neat with clean lines or take on more of an industrial look.
Updates

please note brief has been updated with a more specific description of our business activity

i have also added the final drawing that was used to water-jet the bracket shown in the photos

also, you will note i changed the title to 'logo + business card'

i don't expect a logo as a discrete artefact of the job, however, i expect that some or all elements on the face of the business card will lend themselves to the street sign (as stated in the original brief) as well as any future logo used on letter heads, invoices, etcetera

another update - changed the allowable entries to include logo's only, as well as business cards

Industry/Entity Type

Industrial

Requirements
Must have
• the face should have the name 'Eastgate Joinwerks' (or no/all-caps)

the number '75' in the logo, which will also be turned into a conservative (residential) street sign ('75' being a street number) - '75' should stand alone -OR- be readily identified by someone who has previously received a business card

i need to make this '75' and any associated 'framing', so it should be transferrable to cad/dxf for machining, laser/water-cutting, brazing/welding, etcet.

(on that note, the winning designer will be able to share their vision for this sign and we'll adhere to it ... within the realms of possibility! if you're happy with the result then you could include it in your portfolio)
Nice to have
• one side of the card needs a majority of space for quotes, hand-written information, etcet. so this side should be white or a light, complimentary colour suitable for black/blue pen

the following should appear somewhere on the card (there is no email or website) :
- name : First Last (Proprietor)
- mobile phone number : +61 (0) 498 761203
- abn: 58 907 614 230

any combination of the following (or equivalent) text:

* 'your castle' - this is slang for your house/place (i prefer this to 'home' as 1: it can apply to a place of business, and 2: for me at least, it conjurs images of wrought iron, brass, hardwood & stone)

* unique

* ...

```html
<!DOCTYPE html>
<html lang="en">
<head>
<meta charset="utf-8">
<title>Eastgate Joinwerks — Business Card</title>
<link rel="stylesheet" href="https://fonts.googleapis.com/css2?family=Oswald:wght@500&family=Roboto+Condensed:wght@400&display=swap">
<style>
  :root {
    --page-bg: #e4e5e6;
    --card-brown: #35220f;
    --accent-orange: #f7ae3a;
    --mark-muted: #5e4b3a;
    --note-panel: #e3dfdb;
    --rule-grey: #a8a29b;
    --text-light: #d9cfc3;
    --text-muted: #8f7f6e;
    --decor-brown: #5f4529;
  }
  * { box-sizing: border-box; margin: 0; padding: 0; }
  html, body { width: 1200px; height: 900px; overflow: hidden; }
  body {
    background: var(--page-bg);
    position: relative;
    font-family: "Roboto Condensed", "Arial Narrow", sans-serif;
  }
  .card {
    position: absolute;
    left: 296px;
    width: 606px;
    height: 336px;
    border-radius: 28px;
    background: var(--card-brown);
    overflow: hidden;
  }
  .card--front { top: 70px; }
  .card--back { top: 473px; }

  .brand-square {
    position: absolute;
    left: 263px; top: 108px;
    width: 80px; height: 80px;
    background: var(--mark-muted);
  }
  .front-name {
    position: absolute;
    left: 0; right: 0;
    top: 212px;
    text-align: center;
    font-family: "Oswald", "Arial Narrow", sans-serif;
    font-weight: 500;
    font-size: 27px;
    line-height: 36px;
    letter-spacing: 0.5px;
    color: var(--accent-orange);
    text-transform: uppercase;
  }

  .note-panel {
    position: absolute;
    left: 31px; top: 30px;
    width: 260px; height: 277px;
    border-radius: 10px;
    background: var(--note-panel);
  }
  .note-rule {
    position: absolute;
    left: 18px; right: 17px;
    border-top: 1px dashed var(--rule-grey);
  }
  .abn {
    position: absolute;
    left: 113px; top: 313px;
    font-size: 11px;
    color: var(--text-muted);
  }
  .contact {
    position: absolute;
    left: 309px; top: 44px;
    color: var(--text-light);
  }
  .contact__name { font-size: 20px; line-height: 1.1; }
  .contact__role { font-size: 12px; margin-top: 1px; }
  .contact__phones { margin-top: 30px; font-size: 20px; line-height: 26px; }

  .back-decor-square {
    position: absolute;
    right: 40px; bottom: 34px;
    width: 120px; height: 120px;
    background: var(--decor-brown);
  }
</style>
</head>
<body>
  <section class="card card--front">
    <span class="brand-square" aria-hidden="true"></span>
    <p class="front-name">Eastgate Joinwerks</p>
  </section>

  <section class="card card--back">
    <span class="back-decor-square" aria-hidden="true"></span>

    <div class="note-panel">
      <span class="note-rule" style="top:48px"></span>
      <span class="note-rule" style="top:84px"></span>
      <span class="note-rule" style="top:119px"></span>
      <span class="note-rule" style="top:155px"></span>
      <span class="note-rule" style="top:190px"></span>
      <span class="note-rule" style="top:226px"></span>
      <span class="note-rule" style="top:261px"></span>
    </div>
    <p class="abn">abn. 58 907 614 230</p>

    <div class="contact">
      <p class="contact__name">Tom Harlow</p>
      <p class="contact__role">Proprietor</p>
      <p class="contact__phones">0498 761203<br>+61 (0) 498 761203</p>
    </div>
  </section>
</body>
</html>
```